Film Poster Design For Japanese Film Poster #2

The title of this colour film is KUMO TORI MIZU HOSHI春 夏 秋 冬Translated this is literallySpring Summer Fall Winter ... however the English title is FOUR SEASONSWe attached a series of screen shots from the film and also the computer generated Kanji characters. We will be updating the brief with the Japanese title characters which currently being hand painted.We require the post in two formats. One being the traditional poster format and the other being in a wide screen ration of 1000px by 465px. Same design.This is a drama, feature length film comprising of four separate stories. The is mixture of Japanese and English dialogue. We are looking at 2 possible designs. You can choose to submit either.1: A with lots of white space ... focussing on smaller images at the Japanese text. I have uploaded a sample poster as a very rough indication. "Words nobody says while crossing the bridge" / "Odile Petra June Beaudry" - Lots of white space.Ideally we would have liked to have had the image of the young girl in the kimono pulling on the bell rope clear cut and used on white as a single main image. However, we are not sure that the clarity or resolution of the original image is sufficient. 2: One with lots of images as you can see with the two "Glass Of Rain" Sample posters.Obviously we are not looking for a copy of either poster, but these posters are a guide to the two looks we are after.Thanks. Mayuko
Hello all,Apologies for the delay. We have had to work through some naming issues.The film's English title has had to be renamed to THE LANTERNS. Please do not used PALE HARBOUR in any designed moving forward.Thanks Mayuko Added Sunday, May 25, 2014

```html
<!DOCTYPE html>
<html lang="en">
<head>
<meta charset="utf-8">
<title>KUMO TORI MIZU HOSHI — Film Poster</title>
<link rel="stylesheet" href="https://fonts.googleapis.com/css2?family=Noto+Sans+JP:wght@700&family=Oswald:wght@500;700&display=block">
<style>
  :root {
    --canvas-bg: #d6d6d6;
    --poster-top: #8c8c8c;
    --poster-mid: #c6c6c6;
    --poster-bottom: #ececec;
    --ink: #141414;
    --still-deep: #1c0c22;
    --still-plum: #5a215e;
    --still-rose: #c2457a;
    --still-violet: #5a4bb0;
    --still-ember: #a8333f;
  }

  html, body {
    margin: 0;
    padding: 0;
    width: 1200px;
    height: 600px;
    overflow: hidden;
    background: var(--canvas-bg);
  }

  .canvas {
    position: relative;
    width: 1200px;
    height: 600px;
  }

  .poster {
    position: absolute;
    left: 390px;
    top: 10px;
    width: 420px;
    height: 580px;
    background: linear-gradient(180deg, var(--poster-top) 0%, var(--poster-mid) 45%, var(--poster-bottom) 100%);
    box-shadow: 0 6px 18px rgba(0, 0, 0, 0.25);
    display: flex;
    flex-direction: column;
    align-items: center;
  }

  .poster__kanji {
    display: block;
    margin-top: 40px;
    font-family: "Noto Sans JP", "Hiragino Kaku Gothic ProN", "Yu Gothic", sans-serif;
    font-weight: 700;
    font-size: 270px;
    line-height: 1;
    color: var(--still-plum);
    background:
      radial-gradient(circle at 28% 30%, var(--still-rose) 0%, transparent 38%),
      radial-gradient(circle at 70% 62%, var(--still-violet) 0%, transparent 32%),
      radial-gradient(circle at 55% 18%, var(--still-ember) 0%, transparent 28%),
      linear-gradient(160deg, var(--still-plum) 0%, var(--still-deep) 55%, var(--still-plum) 100%);
    -webkit-background-clip: text;
    background-clip: text;
    -webkit-text-fill-color: transparent;
  }

  .poster__title {
    margin: 26px 0 0;
    font-family: "Oswald", sans-serif;
    font-weight: 700;
    font-size: 27px;
    letter-spacing: 2.5px;
    color: var(--ink);
  }

  .poster__credits {
    margin-top: auto;
    margin-bottom: 30px;
    width: 300px;
    text-align: center;
    color: var(--ink);
    font-family: "Oswald", sans-serif;
  }

  .poster__roles {
    font-weight: 700;
    font-size: 13px;
    letter-spacing: 1px;
    margin: 0 0 4px;
  }

  .poster__billing {
    font-weight: 500;
    font-size: 6.5px;
    line-height: 1.35;
    letter-spacing: 0.4px;
    text-transform: uppercase;
    margin: 0;
  }
</style>
</head>
<body>
  <main class="canvas">
    <article class="poster">
      <span class="poster__kanji" role="img" aria-label="Film still of violet and rose light showing through the character 雲">雲</span>
      <h1 class="poster__title">KUMO TORI MIZU HOSHI</h1>
      <footer class="poster__credits">
        <p class="poster__roles">REALISATOR - PRODUCER - EXECUTIVE PROD</p>
        <p class="poster__billing">Directed by Sora Ueda. Written with Ren Takagi and Aoi Mori. Music by Kaito Sano. Edited by Yuna Ito. Produced at Kawa Films in Tokyo. Coming soon to cinemas.</p>
      </footer>
    </article>
  </main>
</body>
</html>
```